Yoga Studio - Class Timetable Flyer

We require a double sided, size DL (1/3 A4) flyer with our class timetable included.
We would like the final flyer to have.
Side A : Yoga image, logo, address, website, contact phone number, and in big font $40 Introductory Month.
Side B: Clear easy to read timetable, class descriptions and website.
Thank you.
Yours kindly,
Nadia
87d0c7
86cae7
85acd3

```html
<!DOCTYPE html>
<html lang="en">
<head>
<meta charset="utf-8">
<title>Groundwork Studio – Class Timetable Flyer</title>
<link rel="stylesheet" href="https://fonts.googleapis.com/css2?family=Arimo:wght@400;700&family=Raleway:wght@300;400&display=swap">
<style>
  :root {
    --page: #eef1f3;
    --card: #6cbfd2;
    --card-light: #86cae7;
    --card-deep: #4fa9bf;
    --cell: #8fd2ef;
    --cell-line: #b9e4f6;
    --head: #5b6679;
    --ink: #27333f;
    --slate: #4a5a78;
    --white: #ffffff;
    --green: #7cb83a;
    --green-light: #b5d96a;
  }
  * { box-sizing: border-box; margin: 0; padding: 0; }
  html, body { width: 1154px; height: 1200px; overflow: hidden; }
  body {
    background: var(--page);
    font-family: "Arimo", Arial, sans-serif;
    color: var(--ink);
    position: relative;
  }
  .flyer {
    position: absolute;
    top: 80px;
    width: 490px;
    height: 1040px;
    overflow: hidden;
    background: radial-gradient(circle at 50% 62%, var(--card-light) 0%, var(--card) 55%, var(--card-deep) 100%);
    box-shadow: 0 4px 14px rgba(0,0,0,0.25);
  }
  .flyer--front { left: 70px; }
  .flyer--back { left: 594px; }

  /* Front */
  .hero-photo {
    position: absolute; left: 0; top: 0; width: 490px; height: 400px;
    background: linear-gradient(160deg, #e9dccb 0%, #d9c2a8 35%, #7ec3d8 60%, #c98e63 85%, #e77a52 100%);
  }
  .hero-wave { position: absolute; left: 0; top: 300px; width: 490px; height: 160px; }
  .offer-badge {
    position: absolute; left: 8px; top: 336px; width: 220px; height: 220px;
    border-radius: 50%;
    background: radial-gradient(circle at 40% 40%, #ffffff 0%, #eef1f4 70%, #d9dee4 100%);
    border: 8px solid var(--green);
    box-shadow: 0 0 0 4px var(--green-light);
    display: flex; flex-direction: column; justify-content: center;
    padding-left: 44px;
  }
  .offer-price { font-size: 62px; font-weight: 700; color: var(--slate); line-height: 1; letter-spacing: -1px; }
  .offer-label { font-size: 23px; color: var(--slate); line-height: 1.25; margin-top: 6px; }

  .brand {
    position: absolute; left: 0; width: 100%;
    display: flex; flex-direction: column; align-items: center; gap: 18px;
  }
  .brand-dot { width: 84px; height: 84px; border-radius: 50%; background: var(--white); }
  .brand-name {
    font-family: "Raleway", Arial, sans-serif; font-weight: 300;
    color: var(--white); font-size: 50px; line-height: 1; letter-spacing: 1px;
  }
  .flyer--front .brand { top: 610px; }

  .contact {
    position: absolute; left: 0; top: 832px; width: 100%;
    text-align: center; color: var(--ink);
  }
  .contact p { line-height: 1.2; }
  .contact-phone { font-size: 29px; margin-bottom: 14px; }
  .contact-email { font-size: 19px; margin-bottom: 12px; }
  .contact-email strong { font-size: 25px; }
  .contact-label { font-size: 21px; }
  .contact-web { font-size: 24px; font-weight: 700; margin-bottom: 12px; }
  .contact-address { font-size: 21px; }
  .contact strong { font-weight: 700; }

  /* Back */
  .timetable {
    position: absolute; left: 13px; top: 15px; width: 461px;
    border-collapse: collapse; table-layout: fixed;
    font-size: 12px; color: var(--ink);
  }
  .timetable th {
    background: var(--head); color: var(--white); font-weight: 400;
    height: 23px; font-size: 12px; border: 1px solid #6f7a8c;
  }
  .timetable th.time-col { width: 54px; }
  .timetable td {
    background: var(--cell); border: 1px solid var(--cell-line);
    text-align: center; vertical-align: top; padding-top: 5px; line-height: 16px;
  }
  .timetable td.time { text-align: left; padding-left: 5px; }
  .row-930 td { height: 77px; }
  .row-1100 td { height: 60px; }
  .row-1300 td { height: 42px; }
  .row-1630 td { height: 58px; }
  .row-1830 td, .row-1945 td { height: 60px; }

  .flyer--back .brand { top: 412px; gap: 14px; }
  .flyer--back .brand-dot { width: 70px; height: 70px; }
  .flyer--back .brand-name { font-size: 40px; }

  .class-notes {
    position: absolute; left: 26px; top: 562px; width: 436px;
    font-size: 14.5px; line-height: 19px; color: var(--ink); text-align: justify;
  }
  .class-notes p { margin-bottom: 11px; }
  .class-notes strong { font-weight: 700; }
  .class-notes ul { list-style: none; }
  .class-notes li { position: relative; padding-left: 24px; margin-bottom: 11px; }
  .class-notes li::before {
    content: ""; position: absolute; left: 4px; top: 7px;
    width: 6px; height: 6px; border-radius: 50%; background: var(--ink);
  }
  .web-band {
    position: absolute; left: 0; bottom: 0; width: 100%; height: 44px;
    border-top: 4px solid var(--white);
    background: var(--card);
    display: flex; align-items: center; justify-content: center;
    font-size: 23px; font-weight: 700; color: var(--ink);
  }
</style>
</head>
<body>

<section class="flyer flyer--front">
  <div class="hero-photo" role="img" aria-label="Photo of a smiling woman and a man stretching on yoga mats in a bright studio"></div>
  <svg class="hero-wave" viewBox="0 0 490 160" aria-hidden="true">
    <path d="M0 70 C120 40 260 110 490 40 L490 160 L0 160 Z" fill="#6cbfd2"/>
    <path d="M0 70 C120 40 260 110 490 40" fill="none" stroke="#ffffff" stroke-width="10"/>
    <path d="M150 88 C260 110 370 80 490 52" fill="none" stroke="#b9e4f6" stroke-width="4"/>
  </svg>
  <div class="offer-badge">
    <span class="offer-price">$40</span>
    <span class="offer-label">Introductory<br>Month</span>
  </div>

  <div class="brand">
    <span class="brand-dot"></span>
    <span class="brand-name">Groundwork Studio</span>
  </div>

  <div class="contact">
    <p class="contact-phone">Contact us <strong>0400 555 218</strong></p>
    <p class="contact-email">Email Us <strong>nadiamorrow@mailbox.com.au</strong></p>
    <p class="contact-label">Log On</p>
    <p class="contact-web">www.groundworkstudio.com.au</p>
    <p class="contact-address">24 Wattle Grove, Fernvale, Vic-3999</p>
  </div>
</section>

<section class="flyer flyer--back">
  <table class="timetable">
    <thead>
      <tr><th class="time-col"></th><th>MON</th><th>TUES</th><th>WED</th><th>THURS</th><th>FRI</th><th>SAT</th><th>SUN</th></tr>
    </thead>
    <tbody>
      <tr class="row-930"><td class="time">9.30am</td><td></td><td>Hot<br>90 mins</td><td></td><td>Power<br>Vinyasa<br>75 mins</td><td></td><td>Power<br>Vinyasa<br>90 mins</td><td></td></tr>
      <tr class="row-1100"><td class="time">11am</td><td></td><td></td><td></td><td>Power<br>Essentials<br>60 mins</td><td></td><td></td><td></td></tr>
      <tr class="row-1300"><td class="time">1pm</td><td></td><td></td><td>Hot<br>90 mins</td><td></td><td></td><td></td><td></td></tr>
      <tr class="row-1630"><td class="time">4.30pm</td><td></td><td></td><td></td><td></td><td></td><td></td><td>Power<br>Vinyasa<br>90 mins</td></tr>
      <tr class="row-1830"><td class="time">6.30pm</td><td>Power<br>Vinyasa<br>60 mins</td><td></td><td>Hot<br>60 mins</td><td></td><td>Funky<br>Flow<br>75 mins</td><td></td><td>Yin<br>60 mins</td></tr>
      <tr class="row-1945"><td class="time">7.45pm</td><td>Power<br>Essentials<br>60 mins</td><td></td><td>Power<br>Vinyasa<br>60 mins</td><td></td><td></td><td></td><td></td></tr>
    </tbody>
  </table>

  <div class="brand">
    <span class="brand-dot"></span>
    <span class="brand-name">Groundwork Studio</span>
  </div>

  <div class="class-notes">
    <p><strong>Funky Flow</strong> - Finish off the week and head into the weekend with a joyful flowing class to a playlist of funky beats.</p>
    <p>Charity class by donation, suggested $10. Please place cash only in the charity donation box. Frequent guest teachers.</p>
    <p><strong>Hot</strong> - Dynamic sequence of Strength and Breathing exercises. Suitable for beginners. Heat 37 = degrees.</p>
    <p><strong>Power Essentials</strong> - Flowing Practice with space and time to Align and understand the poses deeply, building muscular strength and endurance. Ideal for beginners.</p>
    <p><strong>Power Vinyasa</strong> - Strong, Dynamic, Flowing practice ideal for building physical power, flexibility and mental resilience. Heat = 30 degrees</p>
    <p><strong>Yin</strong> - Long, Slow, Deep practice with a focus on supporting the body to release our deep internal structures of connective tissue.</p>
    <ul>
      <li>Introductory Month only available to first time members.</li>
      <li>Please present concession card and ID for concession prices. Available to full-time students only</li>
    </ul>
  </div>

  <div class="web-band">www.groundworkstudio.com.au</div>
</section>

</body>
</html>
```